Real Estate Company Needs a Contemporary/Modern Business Card Design

We need a Contemporary/Modern Business Card Design for a New Real Estate Company based in San Francisco, CA called Tolvash Orrin Realtors. We would like to see designs that use the color red for the "Tolvash Orrin" and gold for the "Realtors." The design should communicate being Modern and yet Established and Stable.
Updates

Project Deadline Extended
Reason: Waiting for more designs and/or revisions.

Industry/Entity Type

Business

```html
<!DOCTYPE html>
<html lang="en">
<head>
<meta charset="utf-8">
<title>Tolvash Orrin Realtors – Business Card</title>
<link rel="stylesheet" href="https://fonts.googleapis.com/css2?family=Open+Sans:wght@400;600;700&display=swap">
<style>
  :root {
    --page: #e6e6e6;
    --card: #212121;
    --white: #ffffff;
    --soft: #e4e4e4;
    --red: #d9454a;
    --red-dark: #a8262c;
    --gold: #d9b23a;
    --gold-dark: #9c7a1c;
  }
  * { margin: 0; padding: 0; box-sizing: border-box; }
  html, body {
    width: 1200px; height: 894px; overflow: hidden;
    background: var(--page);
    font-family: "Open Sans", Arial, sans-serif;
  }
  .sheet { position: relative; width: 1200px; height: 894px; }
  .card {
    position: absolute; left: 255px;
    width: 690px; height: 394px;
    background: var(--card);
    box-shadow: 0 6px 18px rgba(0,0,0,.25);
    overflow: hidden;
  }
  .card--back { top: 34px; }
  .card--front { top: 466px; }
  .card__trim { position: absolute; inset: 0; width: 100%; height: 100%; }

  .brand { position: absolute; display: flex; align-items: center; gap: 14px; }
  .brand__square { width: 22px; height: 22px; background: var(--red); flex: none; }
  .brand__text { display: flex; flex-direction: column; font-weight: 700; line-height: 1.05; }
  .brand__name { color: var(--red); }
  .brand__trade { color: var(--gold); }
  .card--back .brand { left: 180px; top: 130px; }
  .card--back .brand__text { font-size: 40px; }
  .web {
    position: absolute; left: 180px; top: 246px;
    color: var(--soft); font-size: 21px; letter-spacing: .5px;
  }

  .person { position: absolute; left: 58px; top: 62px; color: var(--white); }
  .person__name { font-size: 24px; font-weight: 700; letter-spacing: .4px; }
  .person__role { font-size: 19px; font-weight: 400; letter-spacing: .6px; margin-top: 2px; }

  .contacts {
    position: absolute; left: 40px; top: 152px; width: 290px;
    list-style: none; color: var(--white); font-size: 15px; text-align: right;
  }
  .contacts li { display: flex; justify-content: flex-end; align-items: center; gap: 8px; height: 23px; }
  .contacts .address { padding-right: 27px; }
  .contacts .gap { height: 10px; }
  .icon { width: 18px; height: 18px; flex: none; }

  .card--front .brand { left: 360px; top: 205px; }
  .card--front .brand__text { font-size: 38px; }
</style>
</head>
<body>
<main class="sheet">

  <section class="card card--back" aria-label="Card back">
    <svg class="card__trim" viewBox="0 0 690 394" aria-hidden="true">
      <defs>
        <linearGradient id="goldBack" x1="0" y1="0" x2="1" y2="1">
          <stop offset="0" stop-color="#9c7a1c"/><stop offset=".5" stop-color="#d9b23a"/><stop offset="1" stop-color="#9c7a1c"/>
        </linearGradient>
        <linearGradient id="redBack" x1="0" y1="0" x2="1" y2="1">
          <stop offset="0" stop-color="#a8262c"/><stop offset=".5" stop-color="#d9454a"/><stop offset="1" stop-color="#a8262c"/>
        </linearGradient>
      </defs>
      <polygon points="120,0 200,0 188,12 120,12" fill="url(#goldBack)"/>
      <polygon points="0,110 12,122 12,300 0,300" fill="url(#redBack)"/>
      <polygon points="678,70 690,58 690,310 678,298" fill="url(#redBack)"/>
      <polygon points="470,382 678,382 690,394 470,394" fill="url(#goldBack)"/>
    </svg>
    <div class="brand">
      <span class="brand__square"></span>
      <span class="brand__text">
        <span class="brand__name">Tolvash Orrin</span>
        <span class="brand__trade">Realtors</span>
      </span>
    </div>
    <p class="web">www.tolvash-orrin.com</p>
  </section>

  <section class="card card--front" aria-label="Card front">
    <svg class="card__trim" viewBox="0 0 690 394" aria-hidden="true">
      <defs>
        <linearGradient id="goldFront" x1="0" y1="0" x2="1" y2="1">
          <stop offset="0" stop-color="#9c7a1c"/><stop offset=".5" stop-color="#d9b23a"/><stop offset="1" stop-color="#9c7a1c"/>
        </linearGradient>
        <linearGradient id="redFront" x1="0" y1="0" x2="1" y2="1">
          <stop offset="0" stop-color="#a8262c"/><stop offset=".5" stop-color="#d9454a"/><stop offset="1" stop-color="#a8262c"/>
        </linearGradient>
      </defs>
      <polygon points="30,0 380,0 372,12 42,12" fill="url(#goldFront)"/>
      <polygon points="392,0 690,0 690,40 678,28 678,12 384,12" fill="url(#redFront)"/>
      <polygon points="0,200 12,212 12,382 0,394" fill="url(#redFront)"/>
      <polygon points="0,394 12,382 260,382 268,394" fill="url(#redFront)"/>
      <polygon points="280,394 288,382 660,382 690,394" fill="url(#goldFront)"/>
      <polygon points="678,300 690,288 690,394 678,382" fill="url(#goldFront)"/>
    </svg>

    <div class="person">
      <h1 class="person__name">CORVIN DELANEY</h1>
      <p class="person__role">GENERAL MANAGER</p>
    </div>

    <ul class="contacts">
      <li class="address">Halden Row 28B</li>
      <li class="address">Brisk Bay, Oakvale</li>
      <li class="gap"></li>
      <li>002 418 570 239
        <svg class="icon" viewBox="0 0 18 18" aria-label="Phone"><circle cx="9" cy="9" r="9" fill="#ffffff"/><path d="M6 4.5l1.6 2-1 1.1c.6 1.4 1.6 2.4 3 3l1.1-1 2 1.6-1 1.6C8.4 12.6 5.4 9.6 4.6 6.3z" fill="#212121"/></svg>
      </li>
      <li>002 418 570 240
        <svg class="icon" viewBox="0 0 18 18" aria-label="Fax"><circle cx="9" cy="9" r="9" fill="#ffffff"/><rect x="5" y="7" width="8" height="5" fill="#212121"/><rect x="6.5" y="4.5" width="5" height="3" fill="none" stroke="#212121"/></svg>
      </li>
      <li>hello@tolvash-orrin.com
        <svg class="icon" viewBox="0 0 18 18" aria-label="Email"><circle cx="9" cy="9" r="9" fill="#ffffff"/><rect x="4.5" y="5.8" width="9" height="6.4" fill="#212121"/><path d="M4.5 5.8l4.5 3.6 4.5-3.6" fill="none" stroke="#ffffff" stroke-width=".9"/></svg>
      </li>
      <li>www.tolvash-orrin.com
        <svg class="icon" viewBox="0 0 18 18" aria-label="Website"><circle cx="9" cy="9" r="9" fill="#ffffff"/><g fill="none" stroke="#212121" stroke-width="1"><circle cx="9" cy="9" r="4.8"/><ellipse cx="9" cy="9" rx="2" ry="4.8"/><path d="M4.2 9h9.6"/></g></svg>
      </li>
    </ul>

    <div class="brand">
      <span class="brand__square"></span>
      <span class="brand__text">
        <span class="brand__name">Tolvash Orrin</span>
        <span class="brand__trade">Realtors</span>
      </span>
    </div>
  </section>

</main>
</body>
</html>
```